Custom Home Page for our new Website

We need a custom home page designed for our new website. We are a successful local copier dealer who is rebuilding our website from scratch. We have decided on Wordpress as our CMS platform and have purchased the professional Corvel theme.

The custom homepage we want will be an imitation of the screen on latest model of copiers we carry. (A picture of this is attached.) the goal is to imitate this style while creating a unique, user-friendly, helpful portal to our website.

The winning entry will make the best transition between the menu structure of our current website (www.hlumo.net) and the new layout.

Target Market(s)

Our target market is small to medium sized businesses in the Southeast US. The users of our site are generally IT professionals looking for drivers/support, gatekeepers or other support staff placing service calls and supply orders or prospects looking for information about our company and products.

Requirements
Must have
• Clean design, no distracting elements
• Modern aesthetic
• A color palette that can be used as a basis for the Skin for the rest of the site (The site's look will be based on the winning homepage design.)
• Simple navigation
• Easy to read
• Easily viewed on both desktop and tablet sized screens
• Our logo
• Easily update-able
• Maximum of 4 of the large squares

```html
<!DOCTYPE html>
<html lang="en">
<head>
<meta charset="utf-8">
<title>Orvo – Home</title>
<link rel="stylesheet" href="https://fonts.googleapis.com/css2?family=Montserrat:wght@300;400;600;700&display=swap">
<style>
:root{
  --page-grey:#f3f3f3;
  --white:#ffffff;
  --ink:#333333;
  --muted:#6b6b6b;
  --brand-red:#a00c30;
  --brand-red-line:#8c0a29;
  --nav-active:#b0102f;
  --hero-dark:#262626;
  --recycle-green:#3c9a2e;
}
*{margin:0;padding:0;box-sizing:border-box}
html,body{width:1200px;height:1131px;overflow:hidden}
body{position:relative;background:var(--page-grey);font-family:"Montserrat",sans-serif;color:var(--ink)}
a{color:inherit;text-decoration:none}
.abs{position:absolute}

.utility-links{left:300px;width:593px;top:19px;text-align:right;font-size:12px;font-weight:300;color:var(--muted);letter-spacing:.3px}
.recycle{left:913px;top:8px;display:flex;align-items:center;gap:6px;font-size:12px;font-weight:600;color:#555}
.recycle-mark{width:41px;height:41px;border-radius:50%;background:var(--recycle-green)}

.site-header{left:122px;top:55px;width:959px;height:79px;background:var(--white)}
.brand{position:absolute;left:18px;top:20px;display:flex;align-items:center;gap:8px;font-size:34px;font-weight:700;color:var(--ink)}
.brand-dot{width:14px;height:14px;border-radius:50%;background:var(--brand-red)}
.main-nav{position:absolute;right:27px;top:31px;display:flex;gap:36px;font-size:15px;font-weight:400;letter-spacing:.3px}
.main-nav .active{color:var(--nav-active)}

.hero{left:122px;top:134px;width:960px;height:307px;background:radial-gradient(circle at 60% 80%,#ffffff 0,#ededed 40%,#dcdcdc 100%)}
.hero-photo{position:absolute;right:0;top:0;width:396px;height:307px;background:linear-gradient(160deg,#6e6e6e 0%,#4a4a4a 40%,#2a2a2a 75%,#1e2a3a 100%)}
.hero-caption{position:absolute;left:0;top:83px;width:400px;height:141px;background:var(--hero-dark);color:#fff;font-size:27px;font-weight:300;padding:50px 0 0 38px;letter-spacing:.5px}
.hero-dots{position:absolute;left:17px;top:275px;display:flex;gap:3px}
.hero-dots span{width:12px;height:12px;border-radius:50%;background:#fff}
.hero-dots .on{background:var(--brand-red)}

.products{left:0;top:478px;width:1200px;height:223px;background:var(--white)}
.products h2{position:absolute;top:10px;width:100%;text-align:center;font-size:22px;font-weight:300;color:#444}
.product-thumb{position:absolute;top:58px;width:221px;height:131px;border:3px solid #fff;box-shadow:0 0 3px rgba(0,0,0,.35)}

.info-card{top:729px;width:300px;height:260px;background:var(--brand-red);color:#fff}
.card-head{height:68px;border-bottom:1px solid var(--brand-red-line);display:flex;align-items:center;gap:14px;padding-left:16px;font-size:14px;font-weight:600}
.card-head svg{flex:none}
.card-body{padding:14px 18px 0 23px;font-size:11.5px;font-weight:300;line-height:19px}
.card-body h3{font-size:15px;font-weight:400;margin:0 0 8px}
.link-list{list-style:none;padding:9px 0 0 38px;font-size:11.5px;font-weight:300}
.link-list li{position:relative;height:27.3px}
.link-list li::before{content:"";position:absolute;left:-23px;top:4px;width:6px;height:6px;border-right:1.5px solid #fff;border-top:1.5px solid #fff;transform:rotate(45deg)}
.quote{text-align:justify}

.site-footer{left:0;top:1028px;width:1200px;height:103px;background:var(--white)}
.footer-nav{position:absolute;left:129px;top:26px;font-size:14px;font-weight:300;color:#555;word-spacing:2px}
.footer-nav span{margin:0 18px}
.copyright{position:absolute;left:129px;top:58px;font-size:14px;font-weight:300;color:#555}
.social{position:absolute;left:961px;top:32px;display:flex;gap:10px}
.social a{width:30px;height:30px;border-radius:50%;background:var(--brand-red)}
</style>
</head>
<body>

<nav class="abs utility-links">Our Philosophy &nbsp;| Our Values | Bill of Rights | Testimonials | Awards | Find Us</nav>
<a class="abs recycle" href="#"><span class="recycle-mark"></span>TONER RECYCLE</a>

<header class="abs site-header">
  <a class="brand" href="#"><span class="brand-dot"></span>Orvo</a>
  <nav class="main-nav">
    <a class="active" href="#">Home</a>
    <a href="#">Who We Are ?</a>
    <a href="#">What We Offer</a>
    <a href="#">Support</a>
    <a href="#">Contact Us</a>
  </nav>
</header>

<section class="abs hero">
  <div class="hero-photo" role="img" aria-label="Dark grey multifunction office copier with touch-screen panel"></div>
  <div class="hero-caption">Business Copier’s /MFP’s</div>
  <div class="hero-dots"><span class="on"></span><span></span><span></span><span></span></div>
</section>

<section class="abs products">
  <h2>Our Products</h2>
  <div class="product-thumb" style="left:130px;background:linear-gradient(135deg,#1a1a1a,#1d4a7a 50%,#111)" role="img" aria-label="Copier touch-screen home menu"></div>
  <div class="product-thumb" style="left:370px;background:linear-gradient(135deg,#9a9a9a,#3f8d74 45%,#5a5a5a)" role="img" aria-label="Copier control panel with green display and keypad"></div>
  <div class="product-thumb" style="left:610px;background:linear-gradient(135deg,#222,#2a5f94 50%,#0e0e0e)" role="img" aria-label="Angled copier touch-screen with icons"></div>
  <div class="product-thumb" style="left:850px;background:linear-gradient(135deg,#bdbdbd,#4fa55a 45%,#333)" role="img" aria-label="Copier panel with pull-out keyboard in use"></div>
</section>

<section class="abs info-card" style="left:130px">
  <div class="card-head">
    <svg width="30" height="40" viewBox="0 0 30 40"><path d="M6 2c3 0 6 7 6 9s-3 3-3 5 4 10 6 12 3-1 5-1 7 4 7 6-4 6-7 6C12 39 3 22 3 10 3 5 4 2 6 2z" fill="#fff"/></svg>
    Orvo Support
  </div>
  <ul class="link-list">
    <li>Download Drivers &amp; Software</li>
    <li>View Kestrel Model Brochures</li>
    <li>Check out Tutorials and Guides</li>
    <li>Connect to a technician</li>
    <li>Toner Pirate Letter</li>
  </ul>
</section>

<section class="abs info-card" style="left:450px">
  <div class="card-head">
    <svg width="42" height="36" viewBox="0 0 42 36"><path d="M21 2C10 2 1 9 1 17c0 5 3 9 8 12l-3 6 9-4c2 0 4 1 6 1 11 0 20-7 20-15S32 2 21 2z" fill="#fff"/><circle cx="13" cy="17" r="2.2" fill="#a00c30"/><circle cx="19" cy="17" r="2.2" fill="#a00c30"/><circle cx="25" cy="17" r="2.2" fill="#a00c30"/><circle cx="31" cy="17" r="2.2" fill="#a00c30"/></svg>
    Testimonials
  </div>
  <div class="card-body">
    <h3>Grace Hall</h3>
    <p class="quote">"The Orvo Team is very knowledgeable and responsive to service calls. They have excellent customer service and very good problem solving skills for both mac and pc users."</p>
    <p style="margin-top:19px">- Dana Whitfield</p>
  </div>
</section>

<section class="abs info-card" style="left:770px">
  <div class="card-head" style="padding-left:10px">
    <svg width="60" height="46" viewBox="0 0 60 46"><circle cx="30" cy="23" r="21" fill="#c9a55a"/><circle cx="30" cy="23" r="15" fill="#7a1020"/></svg>
    IT Friendliness
  </div>
  <div class="card-body">
    <h3>"IT Friendliness"</h3>
    <p style="line-height:23px">Outstanding Achievement<br>View QTL Certificate in pdf format.<br>Read Digital Imaging Review.<br>"IT Friendliness" of its Imager Product.</p>
  </div>
</section>

<footer class="abs site-footer">
  <nav class="footer-nav">Home<span>|</span>Who We Are ?<span>|</span>What We Offer<span>|</span>Support<span>|</span>Contact Us</nav>
  <p class="copyright">Copyright ©2013 &nbsp;Company Name &nbsp;&nbsp;- All rights reserved</p>
  <div class="social"><a href="#" aria-label="Social profile"></a><a href="#" aria-label="Social profile"></a><a href="#" aria-label="Social profile"></a></div>
</footer>

</body>
</html>
```